Harrowvane Business Card

Looking for a new business Card layout for our company, harrowvane.

Standard Business Card , Name, email, phone, website. www.harrowvane.com

```html
<!DOCTYPE html>
<html lang="en">
<head>
<meta charset="utf-8">
<title>Harrowvane Business Card</title>
<link href="https://fonts.googleapis.com/css2?family=Jost:wght@500;600;700&family=Open+Sans:wght@400;600&display=swap" rel="stylesheet">
<style>
  :root {
    --stage: #d8d8d8;
    --label: #5d6a80;
    --card: #ffffff;
    --brand-blue: #4ab5dc;
    --slate: #5a6680;
    --bright-blue: #3cc0e4;
    --white: #ffffff;
  }
  * { box-sizing: border-box; margin: 0; padding: 0; }
  html, body { width: 1200px; height: 858px; overflow: hidden; }
  body { background: var(--stage); position: relative; font-family: "Open Sans", sans-serif; }

  .side-label {
    position: absolute; top: 210px; width: 481px; text-align: center;
    font-family: "Open Sans", sans-serif; font-weight: 600; font-size: 19px;
    color: var(--label); letter-spacing: 0.3px;
  }
  .side-label--front { left: 96px; }
  .side-label--back { left: 623px; }

  .card {
    position: absolute; top: 285px; width: 481px; height: 289px;
    background: var(--card); overflow: hidden;
    box-shadow: 3px 4px 7px rgba(0,0,0,0.35);
  }
  .card--front { left: 96px; }
  .card--back { left: 623px; display: flex; align-items: center; justify-content: center; gap: 12px; }

  .wordmark {
    position: absolute; left: 42px; top: 72px; height: 50px;
    display: flex; align-items: center; gap: 12px;
  }
  .wordmark__dot { width: 34px; height: 34px; border-radius: 50%; background: var(--brand-blue); flex: none; }
  .wordmark__name, .back-mark__name {
    font-family: "Jost", sans-serif; font-weight: 700; font-size: 42px;
    color: var(--brand-blue); text-transform: uppercase; letter-spacing: 0.5px; line-height: 1;
  }

  .info-band {
    position: absolute; left: 0; bottom: 0; width: 100%; height: 111px;
    background:
      radial-gradient(ellipse 160px 110px at 58% 70%, rgba(60,192,228,0.95), rgba(60,192,228,0) 100%),
      radial-gradient(ellipse 120px 90px at 70% 20%, rgba(45,160,210,0.8), rgba(45,160,210,0) 100%),
      var(--slate);
  }
  .holder { position: absolute; left: 41px; top: 31px; color: var(--white); font-family: "Jost", sans-serif; }
  .holder__name { font-weight: 600; font-size: 18px; letter-spacing: 1px; line-height: 1.05; }
  .holder__role { font-weight: 500; font-size: 12.5px; letter-spacing: 1px; line-height: 1.1; }

  .contact-list { position: absolute; left: 271px; top: 18px; list-style: none; color: var(--white); font-size: 13.5px; }
  .contact-list li { display: flex; align-items: center; gap: 7px; height: 20px; }
  .contact-list svg { width: 11px; height: 11px; flex: none; }

  .back-mark__dot { width: 40px; height: 40px; border-radius: 50%; background: var(--brand-blue); }
  .back-mark__name { font-size: 36px; }
</style>
</head>
<body>
  <div class="side-label side-label--front">FRONT</div>
  <div class="side-label side-label--back">BACK</div>

  <section class="card card--front">
    <div class="wordmark">
      <span class="wordmark__dot"></span>
      <span class="wordmark__name">Harrowvane</span>
    </div>
    <div class="info-band">
      <div class="holder">
        <div class="holder__name">CARD HOLDER</div>
        <div class="holder__role">DESIGNATION</div>
      </div>
      <ul class="contact-list">
        <li>
          <svg viewBox="0 0 24 24" fill="#fff"><path d="M6.6 10.8a15.1 15.1 0 0 0 6.6 6.6l2.2-2.2a1 1 0 0 1 1-.25 11.4 11.4 0 0 0 3.6.57 1 1 0 0 1 1 1V20a1 1 0 0 1-1 1A17 17 0 0 1 3 4a1 1 0 0 1 1-1h3.5a1 1 0 0 1 1 1c0 1.25.2 2.45.57 3.57a1 1 0 0 1-.25 1z"/></svg>
          1-555-014-2210
        </li>
        <li>
          <svg viewBox="0 0 24 24" fill="#fff"><path d="M2 9l10-6 10 6v11a1 1 0 0 1-1 1H3a1 1 0 0 1-1-1z"/><path d="M4 10l8 5 8-5" stroke="#5a6680" stroke-width="2" fill="none"/></svg>
          info@harrowvane.com
        </li>
        <li>
          <svg viewBox="0 0 24 24" fill="none" stroke="#fff" stroke-width="2"><circle cx="12" cy="12" r="10"/><path d="M2 12h20M12 2c3 3 3 17 0 20M12 2c-3 3-3 17 0 20"/></svg>
          www.harrowvane.com
        </li>
      </ul>
    </div>
  </section>

  <section class="card card--back">
    <span class="back-mark__dot"></span>
    <span class="back-mark__name">Harrowvane</span>
  </section>
</body>
</html>
```